Design our next "BOLD HORIZON" print. Size 12x36 Horizontal.

I am looking for a poster design with the text "Bold Horizon" . The print size will be a 12x36 inches.(Horizontal) It should have the American flag used throughout the design. I am looking for a very proud feeling. Font can be creative but instantly readable. The design can be old world feel and can also use the deep reds and navy blues.The image does not have to be just the flag and text. It can contain other patriotic symbols. Can also have a grungy feel. I have enclosed our last "Bold Horizon " piece for your reference. We are hoping we can get one even better. Thank You.

• Should Not be like the image example I enclosed. It's just a reference. We need something that is new and different. Plain White text.

```html
<!DOCTYPE html>
<html lang="en">
<head>
<meta charset="UTF-8">
<title>Bold Horizon – 12x36 Banner Print</title>
<link rel="stylesheet" href="https://fonts.googleapis.com/css2?family=Saira+Condensed:wght@800&display=swap">
<style>
  :root {
    --stage-light: #6a6a6a;
    --stage-dark: #3a3a3a;
    --navy: #1e3a6e;
    --navy-deep: #0e1a33;
    --flag-red: #b0102e;
    --flag-red-deep: #5a0616;
    --fabric-white: #d9d9d9;
    --shadow-black: #0a0a0a;
    --type-white: #ffffff;
    --type-silver: #c9ccd0;
  }
  html, body {
    margin: 0;
    padding: 0;
    width: 1200px;
    height: 800px;
    overflow: hidden;
  }
  body {
    background: radial-gradient(ellipse at 50% 35%, var(--stage-light) 0%, var(--stage-dark) 80%);
    position: relative;
    font-family: "Saira Condensed", "Arial Narrow", sans-serif;
  }
  .banner {
    position: absolute;
    left: 30px;
    top: 210px;
    width: 1140px;
    height: 380px;
    overflow: hidden;
    background: var(--shadow-black);
    box-shadow: 0 10px 30px rgba(0,0,0,0.45);
  }
  .banner__flag {
    position: absolute;
    inset: 0;
    width: 100%;
    height: 100%;
    display: block;
  }
  .banner__title {
    position: absolute;
    left: 0;
    right: 0;
    top: 50%;
    transform: translateY(-52%);
    margin: 0;
    text-align: center;
    white-space: nowrap;
    font-weight: 800;
    font-size: 196px;
    line-height: 1;
    letter-spacing: 2px;
    text-transform: uppercase;
    background: linear-gradient(180deg, var(--type-silver) 0%, var(--type-white) 35%, var(--type-white) 55%, var(--type-silver) 100%);
    -webkit-background-clip: text;
    background-clip: text;
    color: transparent;
    filter: drop-shadow(3px 4px 0 rgba(0,0,0,0.85)) drop-shadow(0 0 6px rgba(0,0,0,0.6));
  }
</style>
</head>
<body>
  <section class="banner">
    <svg class="banner__flag" viewBox="0 0 1140 380" preserveAspectRatio="none" role="img" aria-label="Waving, grungy American flag photograph with stars on navy at upper left and red and white stripes in deep shadow">
      <defs>
        <linearGradient id="stripes" x1="0" y1="0" x2="0" y2="1">
          <stop offset="0" stop-color="var(--flag-red-deep)"/>
          <stop offset="0.3" stop-color="var(--flag-red)"/>
          <stop offset="0.5" stop-color="var(--fabric-white)" stop-opacity="0.6"/>
          <stop offset="0.7" stop-color="var(--flag-red)"/>
          <stop offset="1" stop-color="var(--flag-red-deep)"/>
        </linearGradient>
        <radialGradient id="canton" cx="0.15" cy="0.2" r="0.45">
          <stop offset="0" stop-color="var(--navy)"/>
          <stop offset="0.6" stop-color="var(--navy-deep)" stop-opacity="0.8"/>
          <stop offset="1" stop-color="var(--navy-deep)" stop-opacity="0"/>
        </radialGradient>
        <linearGradient id="vignette" x1="0" y1="0" x2="1" y2="0">
          <stop offset="0" stop-color="var(--shadow-black)" stop-opacity="0.5"/>
          <stop offset="0.5" stop-color="var(--shadow-black)" stop-opacity="0"/>
          <stop offset="1" stop-color="var(--shadow-black)" stop-opacity="0.55"/>
        </linearGradient>
      </defs>
      <rect width="1140" height="380" fill="url(#stripes)"/>
      <rect width="1140" height="380" fill="url(#canton)"/>
      <rect width="1140" height="380" fill="url(#vignette)"/>
    </svg>
    <h1 class="banner__title">Bold Horizon</h1>
  </section>
</body>
</html>
```